COVID-19 Related Signage for Hotel

Need to create new COVID-19 related signage utilizing our brand assets. Please use screenshots for copy/direction. essentially duplicate the screenshots but with our logo/branding.

All brand assets have been uploaded and examples of signage content. Pictures are not necessary but you can add them if you want similar to the examples attached.

Sign requirements

sign 1. Text "Hand Sanitizer Station" can add graphic
sign 2. Text "Protect Yourself" duplicate copy in the attached pictures
sign 3. Text "Face Mask Required" can add graphic
sign 4. Text "Face Covering Do's and Don'ts with text from "Face-covering checklist.jpg" REMOVE BWT logo or website or 3 face mask graphics
sign 5. Text "Maintain 6 Foot Distance" This sign will be printed and placed on the ground for guests to know where to stand in queue. Would prefer a circular Design. sign 6. Text "Wet, Lather, Scrub, Rinse, Dry" similar to screenshots attached.

ALL signs should have same look and feel throughout utilizing our brand graphics, logo, colors, and guidelines.

Target Market(s)

Hotel Guests

Industry/Entity Type

Hotel

Font styles to use
Sans Serif

Requirements
Must have
• Cohesive, unified branding look and feel

Should not have
• any use of the word "COVID-19" or Coronavirus.

```html
<!DOCTYPE html>
<html lang="en">
<head>
<meta charset="utf-8">
<title>Hand Sanitizer Station Signage</title>
<link href="https://fonts.googleapis.com/css2?family=Oswald:wght@500;600&display=swap" rel="stylesheet">
<style>
  :root {
    --backdrop: #5f5366;
    --teal: #2bbcc1;
    --teal-deep: #22aeb3;
    --orange: #ff8204;
    --white: #ffffff;
  }
  * { box-sizing: border-box; margin: 0; padding: 0; }
  html, body {
    width: 1200px;
    height: 790px;
    overflow: hidden;
    background: var(--backdrop);
    font-family: "Oswald", "Arial Narrow", sans-serif;
  }
  .canvas {
    position: relative;
    width: 1200px;
    height: 790px;
  }
  .sign {
    position: absolute;
    border: 5px solid var(--white);
    box-shadow: 2px 3px 6px rgba(0, 0, 0, 0.35);
  }
  .sign__pattern {
    position: absolute;
    inset: 0;
    background: linear-gradient(135deg, var(--teal) 0%, var(--teal-deep) 100%);
  }
  .sign__panel {
    position: absolute;
    background: var(--white);
    border-radius: 12px;
  }
  .sign__badge {
    position: absolute;
    border-radius: 50%;
    background: var(--orange);
    border: 5px solid var(--white);
    box-shadow: 0 2px 5px rgba(0, 0, 0, 0.35);
    transform: translate(-50%, -50%);
  }
  .sign__title {
    position: absolute;
    left: 0;
    right: 0;
    text-align: center;
    color: var(--orange);
    font-weight: 600;
    text-transform: uppercase;
    letter-spacing: 0.5px;
  }
  .brand {
    position: absolute;
    display: flex;
    align-items: center;
    gap: 6px;
    transform: translate(-50%, -50%);
    white-space: nowrap;
  }
  .brand__dot {
    width: 12px;
    height: 12px;
    border: 2px solid var(--orange);
    border-radius: 50%;
  }
  .brand__name {
    color: var(--orange);
    font-weight: 500;
  }

  /* Portrait sign */
  .sign--portrait { left: 82px; top: 90px; width: 434px; height: 610px; }
  .sign--portrait .sign__panel { left: 17px; top: 73px; width: 392px; height: 508px; }
  .sign--portrait .sign__badge { left: 212px; top: 113px; width: 188px; height: 188px; }
  .sign--portrait .sign__title { top: 237px; font-size: 78px; line-height: 76px; }
  .sign--portrait .brand { left: 212px; top: 523px; }
  .sign--portrait .brand__name { font-size: 17px; }

  /* Landscape sign */
  .sign--landscape { left: 558px; top: 186px; width: 586px; height: 418px; }
  .sign--landscape .sign__panel { left: 22px; top: 57px; width: 532px; height: 336px; }
  .sign--landscape .sign__badge { left: 288px; top: 87px; width: 140px; height: 140px; }
  .sign--landscape .sign__title { top: 164px; font-size: 70px; line-height: 70px; }
  .sign--landscape .brand { left: 288px; top: 341px; }
  .sign--landscape .brand__name { font-size: 14px; }
</style>
</head>
<body>
<main class="canvas">
  <section class="sign sign--portrait">
    <div class="sign__pattern" role="img" aria-label="Teal swirl pattern border"></div>
    <div class="sign__panel"></div>
    <div class="sign__badge" role="img" aria-label="Icon of a hand under a sanitizer pump bottle"></div>
    <h1 class="sign__title">Hand<br>Sanitizer<br>Station</h1>
    <div class="brand">
      <span class="brand__dot"></span>
      <span class="brand__name">Mill Creek Lodge</span>
    </div>
  </section>

  <section class="sign sign--landscape">
    <div class="sign__pattern" role="img" aria-label="Teal swirl pattern border"></div>
    <div class="sign__panel"></div>
    <div class="sign__badge" role="img" aria-label="Icon of a hand under a sanitizer pump bottle"></div>
    <h1 class="sign__title">Hand Sanitizer<br>Station</h1>
    <div class="brand">
      <span class="brand__dot"></span>
      <span class="brand__name">Mill Creek Lodge</span>
    </div>
  </section>
</main>
</body>
</html>
```